Label for a bottle of Gin soon to launch in the UK.

We need a label for a gin called Halworth Gin. It is very important that the label does not infringe any copyrights of the football club so please avoid the colour blue or anything related to football or the club. The example bottle below shows the bottle that we will be using. The gin will be clear not pink, the use of gold on the label is encouraged.
Should not infringe on the brand shown in the example image.

Club

Sans Serif

• Here is a link to the bottle that the label must fit onto https://www.flaskcrate-depot.co.uk/Glass-bottles/Glass-bottles/700ml-glass-bottles/700ml-clear-glass-bottle-Marosa.html
• No use of blue or anything related to football or Halworth Football Club or Moorhawks. Avoid Red also. White, gold and black should be primary colours used

```html
<!DOCTYPE html>
<html lang="en">
<head>
<meta charset="utf-8">
<title>Halworth Gin – Bottle Label</title>
<link rel="stylesheet" href="https://fonts.googleapis.com/css2?family=Cinzel:wght@500;700&family=Libre+Baskerville&display=swap">
<style>
  :root {
    --canvas: #ffffff;
    --gold: #c29a52;
    --ink: #111111;
    --ice-light: #f4f6f7;
    --ice-mid: #e1e5e8;
    --ice-shadow: #c6ccd0;
  }
  html, body {
    margin: 0;
    padding: 0;
    width: 1200px;
    height: 1200px;
    overflow: hidden;
    background: var(--canvas);
  }
  .label {
    position: relative;
    width: 1200px;
    height: 1200px;
    display: flex;
    flex-direction: column;
    align-items: center;
    box-sizing: border-box;
    padding-top: 200px;
  }
  .brand-name {
    margin: 0;
    font-family: "Cinzel", "Times New Roman", serif;
    font-weight: 500;
    font-size: 104px;
    line-height: 1;
    letter-spacing: 2px;
    color: var(--gold);
  }
  .product-name {
    margin: 10px 0 0;
    font-family: "Cinzel", "Times New Roman", serif;
    font-weight: 700;
    font-size: 300px;
    line-height: 1;
    letter-spacing: 10px;
    color: var(--ink);
  }
  .tagline {
    margin: 24px 0 0;
    font-family: "Libre Baskerville", Georgia, serif;
    font-size: 32px;
    letter-spacing: 4px;
    color: var(--ink);
  }
  .ice-area {
    position: relative;
    margin-top: 30px;
    width: 560px;
    height: 230px;
  }
  .ice-illustration {
    position: absolute;
    inset: 0;
    border-radius: 40px 40px 16px 16px;
    background: linear-gradient(180deg, var(--ice-light) 0%, var(--ice-mid) 55%, var(--ice-shadow) 100%);
  }
  .spec {
    position: absolute;
    top: 130px;
    font-family: "Libre Baskerville", Georgia, serif;
    font-size: 26px;
    color: var(--ink);
  }
  .spec-abv { left: 60px; }
  .spec-volume { right: 90px; }
</style>
</head>
<body>
  <main class="label">
    <h1 class="brand-name">HALWORTH</h1>
    <p class="product-name">GIN</p>
    <p class="tagline">TRADITIONALLY DISTILED</p>
    <div class="ice-area">
      <div class="ice-illustration" role="img" aria-label="Illustration of a pile of clear ice cubes"></div>
      <span class="spec spec-abv">40% vol</span>
      <span class="spec spec-volume">700 ml</span>
    </div>
  </main>
</body>
</html>
```